Create a Graphic About YOURSELF and PixelHarbor

PixelHarbor would like you (designers) to create an awesome graphic to promote YOURSELF and your profile on PixelHarbor!

Your graphic should communicate your name, your services and should mention PixelHarbor.

The design should be perfect for sharing on Chatterly. Here's an example of what we'd like http://blog.pixelharbor-example.ca/article/333/pixelharbor-launches-3000-hire-me-social-design-contest

Once you submitted your design, we'd love you to share the design ('advertisement') and promote yourself and PixelHarbor to your friends and potential customers. So make your submissions great and get your friends to vote for your design by 'Liking' it on Chatterly!

Prizes:
$1500 - "PixelHarbor Community" prize awarded to the designer with the most Chatterly 'Likes'
5 x $50 for the next 5 'most liked' designs on Chatterly

$1000 - "Hire Me" prize awarded to the designer who receives the most client invites
5 x $50 for the next 5 'most invited' designers

In summary, this is a great opportunity for you to increase your exposure to PixelHarbor customers and win cash prizes. Show off your design skills and get hired by PixelHarbor customers from around the world!

Target Market(s)

Fans, friends and customers of YOU

Industry/Entity Type

Cash

Requirements
Must have
• 1) Include your PixelHarbor user name on the graphic so customers can find you in the PixelHarbor Designer Directory
2) Include the tagline "Hire Me on PixelHarbor.com!" in your graphic design.
3) Share your design's URL on our Chatterly wall at http://chatterly-example.com/pixelharbor and get your friends to 'like' your design.
Nice to have
• 1) Include a tagline that expresses your design approach/philosophy
2) Artwork dimensions: 403 x 403 px
3) You can submit more than 1 design!
Should not have
• You must own the copyright of any images you use including stock imagery.

```html
<!DOCTYPE html>
<html lang="en">
<head>
<meta charset="utf-8">
<title>Milo's Graphic Design – Hire Me on PixelHarbor.com!</title>
<link rel="stylesheet" href="https://fonts.googleapis.com/css2?family=Comfortaa:wght@700&family=Oswald:wght@500&family=Tenor+Sans&display=swap">
<style>
  :root {
    --sky-top: #9a68c2;
    --sky-mid: #f4f1f8;
    --sky-low: #dfe9f4;
    --sky-bottom: #98bde0;
    --slogan-grey: #6d6a72;
    --headline-blue: #4c6f90;
    --name-red: #e2262b;
    --name-navy: #2b3a66;
    --service-red: #8e2b4c;
    --hire-brown: #6a2a1c;
    --bubble-edge: rgba(255, 255, 255, 0.85);
  }
  * { margin: 0; padding: 0; box-sizing: border-box; }
  html, body { width: 1200px; height: 1200px; overflow: hidden; }
  body { background: #ffffff; }

  .poster {
    position: relative;
    width: 1200px;
    height: 1200px;
    overflow: hidden;
    background: linear-gradient(175deg,
      var(--sky-top) 0%,
      #c4a6da 18%,
      var(--sky-mid) 42%,
      var(--sky-low) 62%,
      var(--sky-bottom) 100%);
  }

  .bubbles { position: absolute; inset: 0; }

  .swirl-decoration {
    position: absolute;
    left: 770px; top: 470px;
    width: 300px; height: 170px;
    border-radius: 50%;
    background: radial-gradient(ellipse at center, rgba(255,255,255,0.9) 0%, rgba(255,255,255,0.35) 55%, rgba(255,255,255,0) 75%);
    transform: rotate(-12deg);
  }

  .philosophy {
    position: absolute;
    left: 20px; top: 40px;
    font-family: "Comfortaa", sans-serif;
    font-weight: 700;
    font-size: 58px;
    line-height: 1;
    color: var(--slogan-grey);
    text-shadow: 2px 2px 0 #ffffff, -1px -1px 0 #ffffff, 3px 4px 4px rgba(60,40,80,0.35);
    transform: rotate(-24deg);
    transform-origin: left top;
  }
  .philosophy span { display: block; white-space: nowrap; }
  .philosophy .line-1 { margin: 170px 0 0 0; }
  .philosophy .line-2 { margin: 12px 0 0 110px; }
  .philosophy .line-3 { margin: 12px 0 0 90px; }

  .echo-headline {
    position: absolute;
    left: 770px; top: 360px;
    font-family: "Tenor Sans", sans-serif;
    font-size: 42px;
    line-height: 1.15;
    color: #ffffff;
    -webkit-text-stroke: 1px #9aa3ad;
    opacity: 0.85;
    transform: rotate(14deg);
    transform-origin: left top;
    white-space: nowrap;
  }
  .echo-headline span { display: block; }
  .echo-headline .line-2 { margin-left: 40px; }

  .offer {
    position: absolute;
    left: 520px; top: 600px;
    width: 700px;
    text-align: center;
  }
  .headline {
    font-family: "Tenor Sans", sans-serif;
    color: var(--headline-blue);
    font-size: 66px;
    line-height: 80px;
    font-weight: 400;
  }
  .studio-intro {
    margin-top: 12px;
    font-family: "Tenor Sans", sans-serif;
    color: var(--name-navy);
    font-size: 44px;
    line-height: 54px;
  }
  .studio-intro .studio-first { color: var(--name-red); }

  .services {
    list-style: none;
    margin-top: 14px;
    font-family: "Oswald", sans-serif;
    font-weight: 500;
    font-size: 38px;
    line-height: 50px;
    color: var(--service-red);
    text-transform: uppercase;
    text-shadow: 1px 1px 0 #ffffff, 2px 3px 3px rgba(40,20,40,0.35);
  }

  .studio-mark {
    position: absolute;
    left: 30px; top: 670px;
    width: 208px; height: 208px;
    border-radius: 50%;
    background: #ffffff;
    box-shadow: 0 4px 14px rgba(40,60,100,0.25);
    display: flex;
    align-items: center;
    justify-content: center;
    text-align: center;
  }
  .studio-mark-name {
    font-family: "Tenor Sans", sans-serif;
    color: var(--service-red);
    font-size: 30px;
    line-height: 34px;
  }

  .hire-tagline {
    position: absolute;
    left: 0; top: 960px;
    width: 380px;
    text-align: center;
    font-family: "Oswald", sans-serif;
    font-weight: 500;
    font-size: 40px;
    line-height: 62px;
    color: var(--hire-brown);
  }
</style>
</head>
<body>
<main class="poster">

  <svg class="bubbles" width="1200" height="1200" viewBox="0 0 1200 1200" aria-hidden="true">
    <defs>
      <radialGradient id="bubble-fill" cx="38%" cy="32%" r="70%">
        <stop offset="0" stop-color="#ffffff" stop-opacity="0.95"/>
        <stop offset="0.55" stop-color="#e4ecfa" stop-opacity="0.55"/>
        <stop offset="1" stop-color="#b8c8ec" stop-opacity="0.75"/>
      </radialGradient>
    </defs>
    <circle class="bubble" cx="390" cy="566" r="172" fill="url(#bubble-fill)"/>
    <circle class="bubble" cx="525" cy="380" r="100" fill="url(#bubble-fill)" opacity="0.55"/>
    <circle class="bubble" cx="745" cy="478" r="90" fill="url(#bubble-fill)"/>
    <circle class="bubble" cx="985" cy="140" r="82" fill="url(#bubble-fill)"/>
    <circle class="bubble" cx="1128" cy="118" r="60" fill="url(#bubble-fill)"/>
  </svg>

  <div class="swirl-decoration" role="img" aria-label="Soft white swirl of curved light strokes"></div>

  <p class="philosophy">
    <span class="line-1">Great Designs</span>
    <span class="line-2">Start with</span>
    <span class="line-3">Great Customers</span>
  </p>

  <p class="echo-headline" aria-hidden="true">
    <span class="line-1">Advance Your Ideas</span>
    <span class="line-2">Into The Future</span>
  </p>

  <section class="offer">
    <h1 class="headline">Advance Your Ideas<br>Into The Future</h1>
    <p class="studio-intro"><span class="studio-first">Milo's</span> Graphic Design<br>Provides You With</p>
    <ul class="services">
      <li>Photo Retouching, Restoration, Repair</li>
      <li>Logos, Website Banners</li>
      <li>Announcements, Brochures, Events</li>
      <li>HTML &amp; CSS Website Pages</li>
      <li>Posters, Postcards, Labels, Coupons</li>
    </ul>
  </section>

  <div class="studio-mark">
    <p class="studio-mark-name">Milo's<br>Graphic<br>Design</p>
  </div>

  <p class="hire-tagline">“HIRE ME on<br>PixelHarbor.com!”</p>

</main>
</body>
</html>
```